Industry/Entity Type

Business

Contact Information for Business Card

Dane Vorlick - Managing Director

T: 1300 862 519
E: dane@tbwebworks.com.au
W: tbwebworks.com.au

PO BOX 74
MOUNT CLEAR VIC 3350

```html
<!DOCTYPE html>
<html lang="en">
<head>
<meta charset="utf-8">
<title>Business Card – Dane Vorlick – Front and Back</title>
<link rel="stylesheet" href="https://fonts.googleapis.com/css2?family=Anton&family=Nunito+Sans:wght@300;800&display=swap">
<style>
  :root {
    --backdrop: #5e5f5e;
    --card-white: #ffffff;
    --brand-yellow: #fdb913;
    --ink-black: #111111;
    --ink-dark: #2a2a2a;
    --logo-grey: #58595b;
    --band-edge: #4a4b4c;
  }
  html, body {
    margin: 0;
    padding: 0;
    width: 1200px;
    height: 890px;
    overflow: hidden;
    background: var(--backdrop);
  }
  .stage {
    display: block;
    width: 1200px;
    height: 890px;
  }
  .card-front-base { fill: var(--card-white); }
  .card-back-base { fill: var(--brand-yellow); }
  .info-band { fill: var(--brand-yellow); }
  .info-band-edge { fill: var(--band-edge); }
  .logo-word {
    font-family: "Anton", "Oswald", sans-serif;
    font-size: 26px;
    text-anchor: middle;
  }
  .logo-word--brand { fill: var(--brand-yellow); }
  .logo-word--grey { fill: var(--logo-grey); }
  .logo-word--white { fill: var(--card-white); }
  .contact-name {
    font-family: "Nunito Sans", "Helvetica Neue", sans-serif;
    font-weight: 800;
    font-size: 18px;
    fill: var(--ink-black);
    text-anchor: end;
  }
  .contact-line {
    font-family: "Nunito Sans", "Helvetica Neue", sans-serif;
    font-weight: 300;
    font-size: 13.5px;
    fill: var(--ink-dark);
    text-anchor: end;
  }
</style>
</head>
<body>
<svg class="stage" viewBox="0 0 1200 890" xmlns="http://www.w3.org/2000/svg">
  <g class="card card-front">
    <path class="card-front-base" d="M354 178 Q354 154 378 153 L822 134 Q846 133 846 157 L846 412 Q846 436 822 436 L378 436 Q354 436 354 412 Z"/>
    <path class="info-band-edge" d="M600 229 Q600 225 604 225 L846 211 L846 385 L604 375 Q600 375 600 371 Z"/>
    <path class="info-band" d="M604 226 Q604 222 608 222 L846 208 L846 382 L608 372 Q604 372 604 368 Z"/>
    <text class="logo-word logo-word--brand" x="450" y="283">COMPANY</text>
    <text class="logo-word logo-word--grey" x="450" y="313">LOGO</text>
    <text class="contact-name" x="805" y="243">Dane Vorlick</text>
    <text class="contact-line" x="805" y="262">Managing Director</text>
    <text class="contact-line" x="805" y="281">T: 1300 862 519</text>
    <text class="contact-line" x="805" y="299">E: dane@tbwebworks.com.au</text>
    <text class="contact-line" x="805" y="317">W: tbwebworks.com.au</text>
    <text class="contact-line" x="805" y="339">PO BOX 74</text>
    <text class="contact-line" x="805" y="357">MOUNT CLEAR VIC 3350</text>
  </g>
  <g class="card card-back">
    <path class="card-back-base" d="M354 478 Q354 454 378 455 L822 476 Q846 477 846 501 L846 733 Q846 757 822 757 L378 757 Q354 757 354 733 Z"/>
    <text class="logo-word logo-word--white" x="588" y="621">COMPANY</text>
    <text class="logo-word logo-word--white" x="588" y="651">LOGO</text>
  </g>
</svg>
</body>
</html>
```